It is a leisure sector investment company.The company plans to invest in a luxurious 5 star resort

We need a stationery design to our company 'Solmaran Crest Limited' using the winning logo design. We need the letter heads, envelopes & the business cards. Should be simple, plain and professional
Updates
We have upload the source file & vector files which gives our logo design. We prefer the bottom logo.

Have updated under 'must have priorities', the company name, address, tel no. fax no. & the company reg no. which should come on the letter head. the long envelope should have the company name, tel & fax no. 
Business card should have the company name, name on the card, designation, tel no. fax no.  

Industry/Entity Type
Investment
Requirements
Must have
- Letter head details:
Solmaran Crest Limited
14 Floor, North Block, Harbour Meridian Plaza,
Velmont Circus, Colombo 01, Sri Lanka
Tel: +94 11 2764502 Fax: +94 11 2764508
Company Reg No.PB 6192
Long Envelope should have only the company name, adress, Tel & Fax
Business Cards should have the company name, Tel & Fax:
Business Card 1 - Lasantha Wijeratne - Chairman
Business Card 2 - Nuwan.S.Gunawardhana - COO

```html
<!DOCTYPE html>
<html lang="en">
<head>
<meta charset="utf-8">
<title>Solmaran Crest Limited — Business Card</title>
<link rel="stylesheet" href="https://fonts.googleapis.com/css2?family=Cinzel:wght@400&family=Tinos:wght@400&display=swap">
<style>
  :root {
    --page-bg: #ffffff;
    --card-olive: #a3a268;
    --card-olive-dark: #999862;
    --flourish-tone: rgba(120, 118, 78, 0.55);
    --ink-brown: #463b33;
    --label-ink: #111111;
  }
  * { margin: 0; padding: 0; box-sizing: border-box; }
  html, body {
    width: 1200px;
    height: 444px;
    overflow: hidden;
    background: var(--page-bg);
  }
  .sheet {
    position: relative;
    width: 1200px;
    height: 444px;
  }
  .side-label {
    position: absolute;
    top: 24px;
    font-family: "Tinos", "Times New Roman", serif;
    font-size: 21px;
    line-height: 1;
    color: var(--label-ink);
    letter-spacing: 0.02em;
  }
  .side-label--front { left: 73px; }
  .side-label--back { left: 634px; }

  .card {
    position: absolute;
    top: 70px;
    width: 504px;
    height: 305px;
    overflow: hidden;
    background-color: var(--card-olive);
    background-image:
      repeating-linear-gradient(0deg, rgba(255,255,255,0.07) 0 1px, transparent 1px 3px),
      repeating-linear-gradient(90deg, rgba(0,0,0,0.04) 0 1px, transparent 1px 4px);
    color: var(--ink-brown);
    text-align: center;
  }
  .card--front { left: 70px; }
  .card--back { left: 630px; background-color: var(--card-olive-dark); }

  .flourish-backdrop {
    position: absolute;
    left: 0;
    top: 0;
    width: 504px;
    height: 200px;
    background: radial-gradient(ellipse 60% 75% at 50% 35%, var(--flourish-tone) 0%, rgba(120,118,78,0.25) 55%, rgba(120,118,78,0) 100%);
  }
  .crest-emblem {
    position: absolute;
    left: 156px;
    top: 122px;
    width: 196px;
    height: 78px;
    border-radius: 50% / 45%;
    background: radial-gradient(ellipse at 50% 45%, var(--ink-brown) 0%, rgba(70,59,51,0.85) 55%, rgba(70,59,51,0) 100%);
  }

  .company-name {
    position: absolute;
    left: 0;
    width: 100%;
    font-family: "Cinzel", "Trajan Pro", serif;
    font-weight: 400;
    line-height: 1;
    color: var(--ink-brown);
  }
  .company-name__main {
    top: 208px;
    font-size: 46px;
    letter-spacing: 0.01em;
  }
  .company-name__suffix {
    top: 260px;
    font-size: 31px;
    letter-spacing: 0.42em;
    padding-left: 0.42em;
  }

  .contact {
    font-family: "Tinos", "Times New Roman", serif;
    position: absolute;
    left: 0;
    width: 100%;
    line-height: 1;
    color: var(--ink-brown);
  }
  .contact__person { top: 120px; font-size: 17px; letter-spacing: 0.02em; }
  .contact__address { top: 155px; font-size: 10.5px; }
  .contact__phones { top: 183px; font-size: 10.5px; word-spacing: 0.1em; }
</style>
</head>
<body>
  <main class="sheet">
    <div class="side-label side-label--front">FRONT</div>
    <div class="side-label side-label--back">BACK</div>

    <section class="card card--front" aria-label="Business card front">
      <div class="flourish-backdrop" role="img" aria-label="Large faint ornamental flourish decoration"></div>
      <div class="crest-emblem" role="img" aria-label="Company crest emblem"></div>
      <div class="company-name company-name__main">SOLMARAN CREST</div>
      <div class="company-name company-name__suffix">LIMITED</div>
    </section>

    <section class="card card--back" aria-label="Business card back">
      <p class="contact contact__person">Nuwan .S. Gunawardhana - Coo</p>
      <p class="contact contact__address">14, floor, North Block, Harbour Meridian Plaza, Velmont Circus, Colombo 01, Sri Lanka</p>
      <p class="contact contact__phones">Tel No. &nbsp;+94 11 2764502 &nbsp;Fax No. &nbsp;+94 11 2764508</p>
    </section>
  </main>
</body>
</html>
```